Brisbane IT support business needs our first website

Hi All,

We are after a new website design for our IT solutions and support business.The business name is Harlow Digital Systems Group, or HDSG for short. We provide a range of solutions and services within the IT space.

I would like to utilize the two colours in our business logo I have uploaded.

I understand this is initially for the design only aspect of the site, but I would like to engage the winner to finish coding the website and finalize after also.

Target Market(s)

Other businesses owners and home users.

Industry/Entity Type

Business

Requirements
Must have
• Nice clean and functional design utilizing our business colours from the logo.

```html
<!DOCTYPE html>
<html lang="en">
<head>
<meta charset="utf-8">
<title>HDSG — Harlow Digital Systems Group</title>
<link href="https://fonts.googleapis.com/css2?family=Raleway:wght@400;500;600;700;800&family=Open+Sans:wght@400;600;700&family=Noto+Serif:ital@1&display=swap" rel="stylesheet">
<style>
:root{
  --orange:#f05a1a;
  --ink:#2b2e30;
  --text:#666a6d;
  --muted:#9a9ea1;
  --line:#e3e5e6;
  --band:#f6f7f7;
  --footer:#262a2b;
  --footer-low:#1e2122;
  --footer-text:#8d9294;
  --white:#ffffff;
  --green:#4cc23a;
}
*{margin:0;padding:0;box-sizing:border-box}
html,body{width:1200px;height:2275px;overflow:hidden;background:var(--white)}
body{position:relative;font-family:'Open Sans',sans-serif;color:var(--text)}
.abs{position:absolute}

/* header */
.site-header{left:149px;top:0;width:922px;height:72px}
.brand{left:58px;top:20px}
.brand-name{font-family:'Raleway',sans-serif;font-weight:700;font-size:26px;color:var(--ink);letter-spacing:1px}
.main-nav{left:369px;top:0;display:flex}
.nav-item{width:84px;height:72px;text-align:center;padding-top:18px;font-family:'Raleway',sans-serif}
.nav-item b{display:block;font-size:9.5px;font-weight:700;color:var(--ink);letter-spacing:.5px;white-space:nowrap}
.nav-item span{display:block;font-size:8px;color:var(--muted);margin-top:24px;white-space:nowrap}
.nav-item.active{background:var(--orange)}
.nav-item.active b,.nav-item.active span{color:var(--white)}

/* hero */
.hero{left:149px;top:72px;width:922px;height:390px;background:linear-gradient(120deg,#7d8e7a 0%,#a8a48e 35%,#8e8770 60%,#4d5a55 100%)}
.hero-shade{inset:0;background:rgba(40,60,55,.35)}
.hero-title{left:0;width:100%;top:132px;text-align:center;font-family:'Raleway',sans-serif;font-weight:600;font-size:42px;color:var(--white);letter-spacing:2px}
.hero-sub{left:0;width:100%;top:204px;text-align:center;font-family:'Raleway',sans-serif;font-size:16px;line-height:26px;color:var(--white)}
.hero-arrow{top:176px;width:38px;height:38px;background:rgba(40,44,46,.6)}
.hero-arrow.prev{left:0}.hero-arrow.next{right:0}
.hero-arrow svg{display:block;margin:13px auto 0}

/* specialize */
.intro{left:149px;top:462px;width:922px;height:160px;background:var(--band)}
.intro h2{left:50px;top:24px;font-family:'Raleway',sans-serif;font-weight:700;font-size:19px;color:var(--ink);letter-spacing:.5px}
.intro-rule{left:50px;top:62px;width:30px;height:2px;background:var(--ink)}
.intro p{left:50px;top:86px;width:640px;font-size:11px;line-height:19px}
.btn-services{left:685px;top:35px;width:190px;height:35px;background:#363a3c;color:var(--white);font-family:'Raleway',sans-serif;font-weight:700;font-size:11px;letter-spacing:1px;text-align:center;line-height:35px}

/* features */
.feature{top:663px;width:252px}
.feature-photo{width:252px;height:159px;background:linear-gradient(135deg,#5b6f7e,#b7c0c4)}
.feature h3{margin-top:20px;font-family:'Raleway',sans-serif;font-weight:700;font-size:11px;color:var(--ink);letter-spacing:1px}
.feature h4{margin-top:6px;font-family:'Raleway',sans-serif;font-weight:400;font-size:12px;color:var(--muted)}
.feature p{margin-top:12px;font-size:10px;line-height:15px;color:var(--muted)}

/* quote band */
.statement{left:149px;top:998px;width:922px;height:174px;background:linear-gradient(180deg,#dfe5e3,#eef1f0 60%,#e4e9e7)}
.statement p{left:0;width:100%;top:74px;text-align:center;font-family:'Raleway',sans-serif;font-weight:700;font-size:21px;color:#2f3436;letter-spacing:.5px}

/* info row */
.accordion{left:199px;top:1229px;width:330px;height:199px;border:1px solid var(--line)}
.acc-row{border-top:1px solid var(--line);height:31px;display:flex;align-items:center;gap:8px;padding-left:10px;font-family:'Raleway',sans-serif;font-size:10px;font-weight:600;color:var(--ink)}
.acc-row:first-child{border-top:0}
.acc-icon{width:9px;height:9px;border-radius:50%;border:1.5px solid #777}
.acc-body{padding:0 16px 10px 30px;font-size:9px;line-height:14px;color:var(--muted)}
.col-title{font-family:'Raleway',sans-serif;font-weight:600;font-size:13px;color:var(--ink)}
.capabilities{left:549px;top:1231px;width:190px}
.cap{position:relative;margin-top:11px;height:20px}
.cap-label{font-family:'Raleway',sans-serif;font-size:8px;font-weight:700;color:var(--ink);position:absolute;top:6px}
.cap-track{position:absolute;left:0;top:18px;width:190px;height:3px;background:var(--line)}
.cap-fill{position:absolute;left:0;top:18px;height:3px;background:var(--orange)}
.cap-tag{position:absolute;top:0;height:15px;padding:0 4px;background:#2b2e30;color:var(--white);font-size:7px;line-height:15px}
.recent{left:760px;top:1231px;width:260px}
.post{display:flex;gap:10px;margin-top:16px}
.post-thumb{width:34px;height:34px;flex:none;background:linear-gradient(135deg,#6d6a5c,#b6a98c)}
.post h5{font-family:'Raleway',sans-serif;font-weight:500;font-size:10px;line-height:14px;color:var(--ink)}
.post-meta{font-size:8px;color:var(--muted);margin-top:4px}
.stars{color:var(--orange);font-size:9px;letter-spacing:1px}

/* testimonials */
.testimonials{left:149px;top:1514px;width:922px;height:301px;background:var(--band)}
.t-title{left:0;width:100%;top:44px;text-align:center;font-family:'Raleway',sans-serif;font-weight:700;font-size:13px;color:var(--ink);letter-spacing:.5px}
.t-title em{font-style:normal;color:var(--orange)}
.t-avatar{left:436px;top:80px;width:50px;height:50px;border-radius:50%;background:linear-gradient(160deg,#c9b7a5,#8a8078)}
.t-quote{left:150px;width:622px;top:152px;text-align:center;font-family:'Noto Serif',serif;font-style:italic;font-size:16px;line-height:30px;color:#45494b}
.t-name{left:0;width:100%;top:224px;text-align:center;font-family:'Raleway',sans-serif;font-size:9px;font-weight:700;color:var(--ink)}
.t-company{left:0;width:100%;top:239px;text-align:center;font-size:9px;color:var(--muted)}
.t-dots{left:451px;top:262px;display:flex;gap:4px}
.t-dots i{width:5px;height:5px;border-radius:50%;background:#f3b394}
.t-dots i:first-child{background:var(--orange)}

/* footer */
.site-footer{left:149px;top:1815px;width:922px;height:382px;background:var(--footer);color:var(--footer-text)}
.f-col{top:62px;font-size:10px;line-height:16px}
.f-col h6{font-family:'Raleway',sans-serif;font-weight:700;font-size:11px;color:#e9eaea;letter-spacing:1px;margin-bottom:22px}
.f-col strong{color:#d4d6d7}
.f-links li{list-style:none;line-height:20px}
.f-links li::before{content:"›";margin-right:6px}
.f-post{margin-bottom:18px;color:#c7c9ca}
.f-post small{display:block;font-style:italic;color:var(--footer-text);font-size:9px}
.stat b{display:block;font-family:'Raleway',sans-serif;font-size:22px;font-weight:500;color:#eeeeee;line-height:28px}
.stat span{display:block;margin-top:4px;font-size:9px;letter-spacing:1px}
.subscribe{display:flex;margin-top:14px}
.subscribe .field{width:190px;height:24px;background:#1a1d1e;font-size:9px;line-height:24px;padding-left:26px;color:#666}
.subscribe .go{width:60px;height:24px;background:var(--green);color:var(--white);font-size:9px;line-height:24px;text-align:center}
.social-box{display:flex;align-items:center;gap:8px;font-size:8px;line-height:11px;color:#ccc}
.social-box i{width:28px;height:28px;display:block}
.footer-bar{left:149px;top:2197px;width:922px;height:78px;background:var(--footer-low);font-size:8px;color:#5d6264}
.footer-bar .copy{left:50px;top:24px;line-height:16px}
.footer-bar .right{right:50px;top:24px;text-align:right;line-height:16px}
.dots-row{display:flex;gap:12px;justify-content:flex-end;margin-bottom:6px}
.dots-row i{width:7px;height:7px;border-radius:50%;background:#4d5254}
</style>
</head>
<body>

<header class="site-header abs">
  <div class="brand abs"><span class="brand-name">HDSG</span></div>
  <nav class="main-nav abs">
    <div class="nav-item active"><b>HOME</b><span>Lets Start</span></div>
    <div class="nav-item"><b>FEATURES</b><span>Out Of The Box</span></div>
    <div class="nav-item"><b>WHO WE ARE</b><span>What We Do</span></div>
    <div class="nav-item"><b>PORTFOLIO</b><span>Awesome Works</span></div>
    <div class="nav-item"><b>BLOG</b><span>Latest News</span></div>
    <div class="nav-item"><b>LETS TALK</b><span>Contact Us</span></div>
  </nav>
</header>

<section class="hero abs" role="img" aria-label="Photo of two smiling colleagues working together at a laptop">
  <div class="hero-shade abs"></div>
  <h1 class="hero-title abs">WELCOME TO HDSG</h1>
  <p class="hero-sub abs">Create just what you need for your Perfect Website. Choose from a wide range<br>of Elements &amp; simply put them on our website.</p>
  <div class="hero-arrow prev abs"><svg width="8" height="12" viewBox="0 0 8 12"><path d="M7 1L2 6l5 5" stroke="#fff" stroke-width="2" fill="none"/></svg></div>
  <div class="hero-arrow next abs"><svg width="8" height="12" viewBox="0 0 8 12"><path d="M1 1l5 5-5 5" stroke="#fff" stroke-width="2" fill="none"/></svg></div>
</section>

<section class="intro abs">
  <h2 class="abs">WE SPECIALIZE IN ROBUST FINANCIAL SOLUTIONS</h2>
  <div class="intro-rule abs"></div>
  <p class="abs">Lasting change, stakeholders development Marla Quinn world problem solving progressive. Courageous; social entrepreneurship change; accelerate resolve pursue these aspirations asylum.</p>
  <div class="btn-services abs">CHECK OUR SERVICES</div>
</section>

<article class="feature abs" style="left:199px">
  <div class="feature-photo" role="img" aria-label="Photo of hands reviewing printed charts with a pen"></div>
  <h3>WHY CHOOSE US.</h3>
  <h4>Because we are Reliable</h4>
  <p>Lorem ipsum dolor sit amet, consectetur adipiscing elit. Eligendi non, facilis nobis voluptatum est voluptates accusamus molestiae eaque perspiciatis mollitia.</p>
</article>
<article class="feature abs" style="left:483px">
  <div class="feature-photo" role="img" aria-label="Photo of a team gathered around laptops in a busy office" style="background:linear-gradient(135deg,#3b3227,#9a7c55)"></div>
  <h3>OUR MISSION.</h3>
  <h4>To Redefine your Brand</h4>
  <p>Quos, non, esse eligendi ab accusantium voluptatem. Maxime eligendi beatae, atque tempora ullam. Vitae delectus quo, consequuntur rerum molestias quo.</p>
</article>
<article class="feature abs" style="left:767px">
  <div class="feature-photo" role="img" aria-label="Photo of people working at computer screens in a bright studio" style="background:linear-gradient(135deg,#4c5d8a,#c89a5e)"></div>
  <h3>WHAT WE DO.</h3>
  <h4>Make our Customers Happy</h4>
  <p>Porro repellat vero sapiente amet vitae quibusdam necessitatibus consectetur, labore totam. Accusamus perspiciatis asperiores labore esse ab accusantium eos modi sit.</p>
</article>

<section class="statement abs" role="img" aria-label="Soft photo of a calm misty horizon">
  <p class="abs">“EVERYTHING IS DESIGNED, BUT SOME THINGS ARE DESIGNED WELL.”</p>
</section>

<div class="accordion abs">
  <div class="acc-row"><span class="acc-icon"></span>Our Company's Values</div>
  <div class="acc-body">Nullam id dolor id nibh ultricies vehicula ut id elit. Integer posuere erat a ante venenatis dapibus posuere velit aliquet. Duis mollis, est non commodo luctus. Aenean lacinia bibendum nulla sed consectetur.</div>
  <div class="acc-row"><span class="acc-icon"></span>How to get Support?</div>
  <div class="acc-row"><span class="acc-icon"></span>Where can you find us?</div>
  <div class="acc-row"><span class="acc-icon"></span>Why you choose our Company?</div>
</div>

<div class="capabilities abs">
  <div class="col-title">Our Capabilities</div>
  <div class="cap"><span class="cap-label">DUMMY</span><span class="cap-tag" style="left:128px">90%</span><span class="cap-track"></span><span class="cap-fill" style="width:150px"></span></div>
  <div class="cap"><span class="cap-label">DUMMY</span><span class="cap-tag" style="left:88px">60%</span><span class="cap-track"></span><span class="cap-fill" style="width:112px"></span></div>
  <div class="cap"><span class="cap-label">DUMMY</span><span class="cap-tag" style="left:146px">95%</span><span class="cap-track"></span><span class="cap-fill" style="width:170px"></span></div>
  <div class="cap"><span class="cap-label">DUMMY</span><span class="cap-tag" style="left:138px">85%</span><span class="cap-track"></span><span class="cap-fill" style="width:160px"></span></div>
  <div class="cap"><span class="cap-label">DUMMY</span><span class="cap-tag" style="left:108px">70%</span><span class="cap-track"></span><span class="cap-fill" style="width:130px"></span></div>
</div>

<div class="recent abs">
  <div class="col-title">Recently Posted</div>
  <div class="post"><div class="post-thumb" role="img" aria-label="Small photo for baseball news post"></div><div><h5>A Baseball Team Blew Up A Bunch Of Tobias Renn And Dana Wyle Merch</h5><div class="post-meta">20th July, 2014 &nbsp; 42</div></div></div>
  <div class="post"><div class="post-thumb" role="img" aria-label="Small photo of a sunset scene" style="background:linear-gradient(135deg,#c07a4c,#e8c7a0)"></div><div><h5>Want To Know The New 'Sky Raiders' Plot? Then This Is The Post For You</h5><div class="post-meta">20th July, 2014 &nbsp; 42</div></div></div>
  <div class="post"><div class="post-thumb" role="img" aria-label="Small photo of a harbour at night" style="background:linear-gradient(135deg,#6f7a62,#c3b88a)"></div><div><h5>Harbour Lights: Night Watch</h5><div class="post-meta"><span class="stars">★★☆☆☆</span> &nbsp; 40%</div></div></div>
</div>

<section class="testimonials abs">
  <h2 class="t-title abs">WHAT <em>CLIENTS</em> SAY?</h2>
  <div class="t-avatar abs" role="img" aria-label="Client portrait"></div>
  <p class="t-quote abs">"Natus voluptatum enim quod necessitatibus quis expedita harum provident eos obcaecati id culpa corporis molestias."</p>
  <div class="t-name abs">- ROWAN ASHBY</div>
  <div class="t-company abs">Northgate Inc.</div>
  <div class="t-dots abs"><i></i><i></i><i></i></div>
</section>

<footer class="site-footer abs">
  <div class="f-col abs" style="left:50px;width:170px">
    <h6>ABOUT US</h6>
    <p>We believe in Simple, Creative &amp; Flexible Standards.</p><br>
    <p><strong>Headquarters:</strong><br>412 Wexley Lane, Suite 20<br>Harlow Point, CA 90210</p><br>
    <p><strong>Phone:</strong> (55) 0100 200300<br><strong>Fax:</strong> (55) 0100 200301<br><strong>Email:</strong> hello@hdsg.example</p>
  </div>
  <div class="f-col abs" style="left:236px;width:160px">
    <h6>BLOGROLL</h6>
    <ul class="f-links"><li>Documentation</li><li>Feedback</li><li>Plugins</li><li>Support Forums</li><li>Themes</li><li>Studio Blog</li><li>Studio Planet</li></ul>
  </div>
  <div class="f-col abs" style="left:422px;width:170px">
    <h6>RECENT POSTS</h6>
    <p class="f-post">Lorem ipsum dolor sit amet, consectetur<small>20th July, 2014</small></p>
    <p class="f-post">Elit Assumenda vel amet dolorum quasi<small>20th July, 2014</small></p>
    <p class="f-post">Debitis nihil placeat, illum est nisi<small>20th July, 2014</small></p>
  </div>
  <div class="f-col abs" style="left:619px;width:260px">
    <div style="display:flex;gap:34px"><div class="stat"><b>15,065,421</b><span>TOTAL VIEWS</span></div><div class="stat"><b>18,465</b><span>CLIENTS</span></div></div>
    <p style="margin-top:26px;color:#d4d6d7">Subscribe to Our Newsletter to get Important News.</p>
    <p style="margin-top:8px;color:#d4d6d7">Subscribe to Our Newsletter to get Important News, Amazing Offers &amp; Inside Scoops:</p>
    <div class="subscribe"><div class="field">Enter your Email</div><div class="go">subscribe</div></div>
    <div style="display:flex;gap:40px;margin-top:16px">
      <div class="social-box"><i style="background:#2f5fa8"></i><span>Like us<br>on our page</span></div>
      <div class="social-box"><i style="background:#e8731d"></i><span>Subscribe<br>to news feed</span></div>
    </div>
  </div>
</footer>
<div class="footer-bar abs">
  <div class="copy abs">Copyright © 2014 All Rights Reserved<br>Terms of Use / Privacy Policy</div>
  <div class="right abs"><div class="dots-row"><i></i><i></i><i></i><i></i><i></i><i></i><i></i><i></i></div>hello@hdsg.example &nbsp; +55 0100 200300 &nbsp; Online</div>
</div>

</body>
</html>
```